Bottled Margarita Label Project

We need a label design (using a 750 ml bottle) for an all natural, premium, Ready to Drink (as in pre-mixed) Margarita. The brand is called KOVENTA Pure Margarita. We were tired of the chemical, sugary, preservative laden "margaritas" with artificial colorings and cheap tequilas, so we developed a simple, straightforward CLASSIC, ingredient driven margarita made with only the purest, traditional ingredients: 100% Blue Agave Tequila Reposado, Double Distilled Orange Liqueur, Lime Juice and sweetened with Organic Cane Sugar. The result is a pure margarita, the kind you got on that amazing beach vacation in Mexico. This is a product that can be chilled and served over ice or straight up. You might grab one to take to a BBQ or to the beach. It's simple, sexy and classic. We are hoping the final design can communicate purity, integrity of ingredients and the freedom one might feel when on vacation in the sun. This doesnt have to be a Latin themed beverage, but more of a Summer / chill / "sol de brisa" in a bottle vibe. Thank you!

Target Market(s)

25 to 45 year olds who feel they know what makes up a good margarita. Aspirational types who love adventurous vacations but are not necessarily wealthy. Our customer doesn't always have the time to make a real margarita from scratch but wish they could get a decent one in a bottle that doesn't taste artificial. They are brand and label conscious and will pay a little more for quality as long as there is value.

Industry/Entity Type

Cafe

Requirements
Must have
• Must have "Koventa" and "pure margartia" clearly listed as the name of the beverage. Must also make clear that this is "Premium", "Ready to Drink" and "Made with 100% Blue Agave Tequila"
Nice to have
• We really love designs that are clean and uncluttered. We have imagined a clear 750ml bottle. Think about tequila when you think about this label. This is a hand made, artisan product produced in batches. We are looking for a finished label/bottle that is colorful, transcendent, artisinal and timeless. It should be mature but not stuffy. It should be simple and sexy - not splashy, brash or silly. Our competition is Dainty Lass Margarita, Tomas Varela, and Ruvel pre-mixed margaritas which are fake margaritas made in huge factories. Koventa is made with integrity and honest ingredients. For colors, greens come to mind but we are totally open to a designer's vision ;). This should be a product that a fashion forward airline like Halcyon Airways would want serve and a bottle that a savvy drinker would choose over the bland, mainstream brands. Check out Morvane Jantra for a sexy, vibrant take on a bottle of alcohol with a Summer slant. Also look at Tervolune tequila. They have a wonderful label that blends vintage and modern elements with minimalist design and comes off as handmade.
Should not have
• Elements we do NOTwant to see any red colors, sombreros, parrots, tiki masks, palm trees, spring break, deserted islands, or Dwight Fennick imagery. This should be a product that an airline like Halcyon Airways would want to serve.

```html
<!DOCTYPE html>
<html lang="en">
<head>
<meta charset="utf-8">
<title>Koventa Pure Margarita – Bottle Label</title>
<link rel="stylesheet" href="https://fonts.googleapis.com/css2?family=Uncial+Antiqua&family=Marcellus&family=Cormorant+Garamond:ital,wght@1,600&display=swap">
<style>
  :root {
    --backdrop: #2f4a1e;
    --label-field: #c6ae24;
    --label-field-deep: #b39a1a;
    --frame-black: #17120d;
    --frame-silver: #a9a9a4;
    --ink: #17120d;
    --band-text: #d8d8d2;
  }
  html, body {
    margin: 0;
    padding: 0;
    width: 1200px;
    height: 1000px;
    overflow: hidden;
    background: var(--backdrop);
  }
  .canvas {
    position: relative;
    width: 1200px;
    height: 1000px;
  }
  .label {
    position: absolute;
    inset: 0;
    width: 1200px;
    height: 1000px;
  }
  .frame-outer { fill: var(--frame-black); }
  .frame-rule { fill: none; stroke: var(--frame-silver); stroke-width: 3; }
  .field { fill: url(#fieldTone); }
  .premium-band { fill: var(--frame-black); }
  .premium-band-edge { fill: none; stroke: var(--frame-silver); stroke-width: 3; }
  .premium-word {
    font-family: "Marcellus", serif;
    font-size: 52px;
    letter-spacing: 2px;
    fill: var(--band-text);
  }
  .brand-name {
    font-family: "Uncial Antiqua", serif;
    font-size: 124px;
    fill: var(--ink);
  }
  .product-line {
    font-family: "Uncial Antiqua", serif;
    font-size: 48px;
    fill: var(--ink);
  }
  .tagline,
  .serve-note {
    font-family: "Cormorant Garamond", serif;
    font-style: italic;
    font-weight: 600;
    fill: var(--ink);
  }
  .tagline { font-size: 40px; }
  .serve-note { font-size: 32px; letter-spacing: 1px; }
</style>
</head>
<body>
<main class="canvas">
  <svg class="label" viewBox="0 0 1200 1000" xmlns="http://www.w3.org/2000/svg" role="group" aria-label="Koventa Pure Margarita label">
    <defs>
      <linearGradient id="fieldTone" x1="0" y1="0" x2="1" y2="1">
        <stop offset="0" stop-color="var(--label-field)"/>
        <stop offset="1" stop-color="var(--label-field-deep)"/>
      </linearGradient>
      <clipPath id="fieldClip">
        <rect x="292" y="40" width="614" height="925" rx="46"/>
      </clipPath>
    </defs>

    <!-- label frame -->
    <rect class="frame-outer" x="262" y="10" width="674" height="985" rx="70"/>
    <rect class="frame-rule" x="276" y="24" width="646" height="957" rx="60"/>
    <rect class="field" x="292" y="40" width="614" height="925" rx="46"/>

    <!-- premium band -->
    <g clip-path="url(#fieldClip)">
      <polygon class="premium-band" points="292,225 292,330 680,40 545,40"/>
      <polyline class="premium-band-edge" points="292,340 694,40"/>
    </g>
    <text class="premium-word" transform="translate(300 292) rotate(-36.8)">PREMIUM</text>

    <!-- brand name -->
    <text class="brand-name" x="599" y="560" text-anchor="middle">Koventa</text>

    <!-- product line -->
    <text class="product-line" x="672" y="682" text-anchor="middle">pure margarita</text>

    <!-- tagline -->
    <text class="tagline" x="578" y="826" text-anchor="middle">Made with 100% Blue Agave Tequila</text>

    <!-- serving note -->
    <text class="serve-note" x="599" y="892" text-anchor="middle">Ready to Drink</text>
  </svg>
</main>
</body>
</html>
```